GUARANTEED WordPress design needed for a sassy, confident charisma coach!

We need a website design for Mira Haskett's brand new, responsive, Wordpress website.
Mira is a trainer / coach who teaches people how to be more charismatic and runs events, publishes video courses and has an ongoing video blog. Her old website is here: www.mirahaskett-example.co.uk ... but it's now time to have a much better site!
We have a strong idea about the technical components of the website, but we need a designer's eye to create a great style for the site (and provide layered PSD files which our developers will then convert to HTML and CSS).
Mira's brand is sassy, brave, warm and confident. The videos on her existing site give quite a good feel for her personality. We need a clean, stylish and compelling page that isn't too corporate and captures her personality. Every element needs to feel coherent, from fonts and headings to colours and spacing.
The following sites are not exactly what Mira wants (and certainly aren't right in terms of colours) but they give you an idea of the kind of people she is competing against and the area she is operating in:
http://www.fenna-troske.example/
http://brynwellow.example/
Ideally, you will have done something similar and be able to key in on exactly the kind of thing we want: we're not looking to reinvent the wheel. Hopefully you won't mind tweaking a few things if you are close to what we need.
More detail is provided in the word document attached. But in a nutshell we need: a banner, footer, sign-up strap, menu bar, signature and 4 different basic page types. We want bursts of bright colours, contrasted with black and white if possible - sorry we can't be more specific than that...
The word doc also contains some amateur mock-ups as well (the images are also just mockups at this stage) - but although these give a general sense of the structure what we are looking for, we are clearly not designers...so please help! We need a designer's touch!
Kind regards,
Tomas
PS The layered PSD versions of the mockup files are available on Quellbox: https://files.quellbox.example/sh/k27rpw4m1xqzv/QWxnEr8tLpVu3YcMd0aHs?dl=0
Project Deadline Extended Reason: We are looking for a polished, "designed" look. The mock-up that we have provided is just indicative of the features we want. Added Saturday, May 14, 2016
Entrepreneurs who need to sell themselves.
4 page

```html
<!DOCTYPE html>
<html lang="en">
<head>
<meta charset="utf-8">
<title>Mira Haskett — Charisma Coach</title>
<link rel="stylesheet" href="https://fonts.googleapis.com/css2?family=Raleway:ital,wght@0,300;0,400;0,500;0,600;0,700;0,800;1,600&display=swap">
<style>
:root{
  --magenta:#e940c0;
  --lime:#b4d11c;
  --green:#8cee3a;
  --cyan:#14c4ee;
  --red:#ef1f1f;
  --ink:#1e1e1e;
  --grey:#8d8d8d;
  --light:#f1f1f1;
  --line:#dedede;
  --dark:#2b2b2b;
  --white:#ffffff;
}
*{box-sizing:border-box;margin:0;padding:0}
html,body{width:1200px;height:3422px;overflow:hidden}
body{font-family:"Raleway",Arial,sans-serif;color:var(--ink);background:var(--light);position:relative}
.abs{position:absolute}

/* header */
.site-header{left:0;top:0;width:1200px;height:84px;background:var(--white);border-bottom:1px solid var(--line)}
.brand{left:64px;top:20px;font-size:40px;font-weight:500;color:var(--ink);letter-spacing:.5px}
.main-nav{right:78px;top:28px;display:flex;gap:6px}
.main-nav a{font-size:13px;font-weight:700;color:var(--ink);text-decoration:none;padding:7px 12px;letter-spacing:.3px}
.main-nav a.current{border:1px solid #9a9a9a}

/* hero */
.hero{left:0;top:84px;width:1200px;height:596px;background:var(--white)}
.hero-tags{left:59px;top:76px}
.hero-tags span{display:block;width:max-content;background:var(--magenta);color:var(--white);font-size:68px;font-weight:300;line-height:70px;padding:2px 18px 0 16px;margin-bottom:5px;letter-spacing:1px}
.hero-portrait{left:696px;top:19px;width:376px;height:428px;background:linear-gradient(180deg,#ffffff 0%,#f3d7d7 35%,#e0303a 70%,#d22a33 100%);border-radius:40% 40% 6px 6px}
.optin{left:0;top:446px;width:1200px;height:150px;background:var(--lime)}
.laptop{left:70px;top:356px;width:380px;height:220px}
.laptop-screen{position:absolute;left:10px;top:0;width:312px;height:205px;background:linear-gradient(180deg,#2a2a2a,#3c3c3c);border-radius:10px 10px 0 0}
.laptop-base{position:absolute;left:0;top:205px;width:380px;height:15px;background:linear-gradient(180deg,#d8d8d8,#b8b8b8);border-radius:0 0 8px 8px}
.optin-copy{left:424px;top:10px;width:560px;font-size:17px;line-height:23px;font-weight:500;color:var(--ink)}
.optin-copy strong{color:#7a1ea8;font-weight:800}
.field{background:var(--white);border:1px solid #d0d0d0;font-size:12px;color:#8a8a8a;padding:0 9px;display:flex;align-items:center;height:36px}
.btn-red{background:var(--red);color:var(--white);font-weight:700;font-size:13px;display:flex;align-items:center;justify-content:center;height:36px}
.optin .f1{left:427px;top:70px;width:193px}
.optin .f2{left:634px;top:70px;width:192px}
.optin .go{left:839px;top:70px;width:103px}
.promise{left:456px;top:116px;font-size:12px;color:var(--red)}

/* posts */
.post{left:80px;width:684px;height:527px;background:var(--white);box-shadow:0 2px 4px rgba(0,0,0,.18)}
.post-banner{position:absolute;left:11px;top:11px;width:659px;height:334px;overflow:hidden}
.post-banner .photo{position:absolute}
.post-banner h2{position:absolute;color:var(--white);font-weight:400;text-transform:uppercase;letter-spacing:.5px}
.post-title{position:absolute;left:11px;top:372px;font-size:19px;font-weight:700;letter-spacing:.2px}
.post-excerpt{position:absolute;left:11px;top:400px;width:650px;font-size:12.5px;line-height:20px;color:var(--grey)}
.post-excerpt a{color:var(--red);text-decoration:none}
.post-meta{position:absolute;left:11px;top:480px;display:flex;gap:40px;font-size:10.5px;color:var(--grey);text-transform:uppercase}
.post-meta span{display:flex;align-items:center;gap:10px}

.bg-red{background:var(--red)}
.bg-green{background:var(--green)}
.bg-cyan{background:var(--cyan)}
.bg-magenta{background:var(--magenta)}

/* pagination */
.pager{left:306px;top:2996px;display:flex;gap:11px}
.pager span{width:26px;height:26px;border-radius:50%;border:1.5px solid #9a9a9a;font-size:11px;color:#777;display:flex;align-items:center;justify-content:center}
.pager span.current{background:#9a9a9a;color:var(--white)}

/* sidebar */
.widget{left:792px;width:326px;background:var(--white);box-shadow:0 1px 3px rgba(0,0,0,.15)}
.widget h3{font-size:19px;font-weight:600;padding:14px 16px 8px;border-bottom:1px solid var(--line);margin:0 0 0;letter-spacing:.3px}
.quotes{padding:0 16px}
.quotes li{list-style:none;border-bottom:1px solid var(--line);padding:14px 0 10px}
.quotes li:last-child{border-bottom:none}
.quotes p{font-size:12.5px;line-height:17px;color:var(--ink)}
.quotes small{display:flex;gap:10px;align-items:center;margin-top:8px;font-size:9.5px;color:var(--grey);text-transform:uppercase}
.tag-cloud{width:240px;margin:17px auto 0;display:flex;flex-wrap:wrap;justify-content:center;gap:4px}
.tag-cloud span{color:var(--white);padding:1px 5px;line-height:1.2}
.t-s{font-size:12px}
.t-l{font-size:25px;font-weight:500}
.t-c{background:var(--cyan)} .t-r{background:var(--red)} .t-m{background:var(--magenta)} .t-g{background:#8fd436}

.promo{position:absolute;left:18px;top:66px;width:290px;height:657px;background:#111;overflow:hidden}
.promo .photo{position:absolute;left:0;top:0;width:290px;height:430px;background:linear-gradient(180deg,#e8e8e8 0%,#9c9c9c 45%,#2a2a2a 100%)}
.promo .strap{position:absolute;left:-6px;top:300px;width:320px;height:130px;background:#a2f03c;transform:rotate(-14deg);display:flex;align-items:center;justify-content:center}
.promo .strap p{font-size:31px;line-height:33px;font-weight:500;color:#111;text-transform:uppercase;text-align:center}
.promo .live{position:absolute;left:57px;top:446px;width:176px;height:72px;background:#f21c1c;border-radius:8px;color:var(--white);font-size:56px;font-weight:600;display:flex;align-items:center;justify-content:center;letter-spacing:2px}
.promo .places{position:absolute;left:22px;top:540px;color:var(--white);font-style:italic;font-weight:600;font-size:26px}
.promo .more{position:absolute;left:0;bottom:0;width:290px;height:47px;background:var(--magenta);color:var(--white);font-weight:600;font-size:22px;display:flex;align-items:center;justify-content:center}

/* signup */
.signup{left:0;top:3075px;width:1200px;height:244px;background:var(--red);color:var(--white);text-align:center}
.signup h4{position:absolute;left:0;top:26px;width:1200px;font-size:27px;line-height:33px;font-weight:500}
.signup .f1{left:276px;top:130px;width:247px;height:43px}
.signup .f2{left:535px;top:130px;width:250px;height:43px}
.signup .go{left:796px;top:130px;width:130px;height:43px;background:var(--lime);color:var(--ink);font-size:15px}
.signup .sad{position:absolute;left:0;top:188px;width:1200px;font-size:15px}

/* footer */
.site-footer{left:0;top:3319px;width:1200px;height:103px;background:var(--dark);color:#9a9a9a}
.site-footer .copy{left:80px;top:34px;font-size:12px}
.legal{left:80px;top:62px;display:flex;gap:38px;font-size:10.5px;text-transform:uppercase}
.social{left:846px;top:33px;display:flex;gap:10px}
.social span{width:36px;height:36px;background:#5f6f7d;border-radius:4px}
</style>
</head>
<body>

<header class="site-header abs">
  <div class="brand abs">Mira Haskett</div>
  <nav class="main-nav abs">
    <a class="current">HOME</a><a>EVENTS</a><a>WORK WITH ME</a><a>CORPORATE</a><a>ABOUT</a><a>CONTACT</a>
  </nav>
</header>

<section class="hero abs">
  <div class="hero-tags abs"><span>ATTRACT</span><span>CONNECT</span><span>INFLUENCE</span></div>
  <div class="hero-portrait abs" role="img" aria-label="Photo of Mira in a red dress, hands on hips"></div>
  <div class="optin abs">
    <p class="optin-copy abs">Learn how to unlock the superpower* of your charisma and win all the business you want with this <strong>FREE training.</strong></p>
    <div class="field f1 abs">First Name</div>
    <div class="field f2 abs">Email Address</div>
    <div class="btn-red go abs">Yes Please</div>
    <p class="promise abs">* Promise to only use your powers for good</p>
  </div>
  <div class="laptop abs" role="img" aria-label="Laptop showing a training video of Mira">
    <div class="laptop-screen"></div>
    <div class="laptop-base"></div>
  </div>
</section>

<article class="post abs" style="top:707px">
  <div class="post-banner bg-red">
    <div class="photo" style="left:0;top:0;width:659px;height:334px;background:linear-gradient(90deg,#ef2424,#d81818)" role="img" aria-label="Mira speaking on stage before an audience"></div>
    <div class="photo" style="left:450px;top:70px;width:150px;height:264px;background:linear-gradient(180deg,#f05a4a,#b5121a);border-radius:40% 40% 0 0" role="img" aria-label="Mira with microphone"></div>
    <h2 style="left:25px;top:80px;font-size:39px;line-height:52px">Public<br>Speaking...</h2>
  </div>
  <h3 class="post-title">PUBLIC SPEAKING...MADE EASY</h3>
  <p class="post-excerpt">Lorem ipsum dolor sit amet, consectetur adipiscing elit. Praesent fringilla tortor et mi convallis, ut scelerisque dui rhoncus. Donec quis lorem malesuada, molestie metus id, vehicula lacus. Pellentesque ultricies venenatis ullamcorper. Sed metus ligula, pharetra id risus eu. <a>Continue Reading</a></p>
  <div class="post-meta"><span>▦ MAY 1ST 2016</span><span>◔ 21 COMMENTS</span></div>
</article>

<article class="post abs" style="top:1280px">
  <div class="post-banner bg-green">
    <div class="photo" style="left:455px;top:120px;width:190px;height:214px;background:linear-gradient(180deg,#6fb33a,#2a3a6a);border-radius:45% 45% 0 0" role="img" aria-label="Mira smiling"></div>
    <h2 style="left:25px;top:28px;font-size:42px;line-height:52px">How to start every<br>day in the right<br>frame of mind!</h2>
    <h2 style="left:25px;top:215px;font-size:62px;line-height:70px">5 hot tips</h2>
  </div>
  <h3 class="post-title">HOW TO START EVERY DAY IN THE RIGHT FRAME OF MIND!</h3>
  <p class="post-excerpt">Lorem ipsum dolor sit amet, consectetur adipiscing elit. Praesent fringilla tortor et mi convallis, ut scelerisque dui rhoncus. Donec quis lorem malesuada, molestie metus id, vehicula lacus. Pellentesque ultricies venenatis ullamcorper. Sed metus ligula, pharetra id risus eu. <a>Continue Reading</a></p>
  <div class="post-meta"><span>▦ MAY 1ST 2016</span><span>◔ 21 COMMENTS</span></div>
</article>

<article class="post abs" style="top:1855px">
  <div class="post-banner bg-cyan">
    <div class="photo" style="left:460px;top:150px;width:155px;height:184px;background:linear-gradient(180deg,#ffffff,#f2c8c8)" role="img" aria-label="Style guide book cover with Mira and a red dress"></div>
    <h2 style="left:25px;top:28px;font-size:42px;line-height:52px">Take charge of your<br>style...</h2>
    <h2 style="left:25px;top:165px;font-size:42px;line-height:52px">...boost your<br>confidence</h2>
  </div>
  <h3 class="post-title">TAKE CHARGE OF YOUR STYLE...BOOST YOUR CONFIDENCE</h3>
  <p class="post-excerpt">Lorem ipsum dolor sit amet, consectetur adipiscing elit. Praesent fringilla tortor et mi convallis, ut scelerisque dui rhoncus. Donec quis lorem malesuada, molestie metus id, vehicula lacus. Pellentesque ultricies venenatis ullamcorper. Sed metus ligula, pharetra id risus eu. <a>Continue Reading</a></p>
  <div class="post-meta"><span>▦ MAY 1ST 2016</span><span>◔ 21 COMMENTS</span></div>
</article>

<article class="post abs" style="top:2423px">
  <div class="post-banner bg-magenta">
    <div class="photo" style="left:470px;top:20px;width:170px;height:314px;background:linear-gradient(180deg,#d36fb8,#4a3a30);border-radius:45% 45% 0 0" role="img" aria-label="Mira gesturing while talking"></div>
    <h2 style="left:25px;top:22px;font-size:40px;line-height:53px">Unfulfilled? It's<br>time to think<br>about your<br>values...</h2>
    <h2 style="left:25px;top:262px;font-size:24px;line-height:30px;color:#2a1530;font-weight:500">Do this exercise now!</h2>
  </div>
  <h3 class="post-title">UNFULFILLED? IT'S TIME TO THINK ABOUT YOUR VALUES...</h3>
  <p class="post-excerpt">Lorem ipsum dolor sit amet, consectetur adipiscing elit. Praesent fringilla tortor et mi convallis, ut scelerisque dui rhoncus. Donec quis lorem malesuada, molestie metus id, vehicula lacus. Pellentesque ultricies venenatis ullamcorper. Sed metus ligula, pharetra id risus eu. <a>Continue Reading</a></p>
  <div class="post-meta"><span>▦ MAY 1ST 2016</span><span>◔ 21 COMMENTS</span></div>
</article>

<nav class="pager abs"><span class="current">1</span><span>2</span><span>3</span><span>…</span><span>15</span><span>»</span></nav>

<aside class="widget abs" style="top:707px;height:365px">
  <h3>MIRA SAYS</h3>
  <ul class="quotes">
    <li><p>"Be more dog: 5 lessons we could learn from our best friends"</p><small>▦ MAY 1ST 2016</small></li>
    <li><p>"Are you letting your core beliefs hold you back?"</p><small>▦ MAY 1ST 2016</small></li>
    <li><p>"How I learned to stop worrying and start NETWORKING!"</p><small>▦ MAY 1ST 2016</small></li>
    <li><p>"Bitchy resting face and other strange - but true - problems"</p><small>▦ MAY 1ST 2016</small></li>
  </ul>
</aside>

<aside class="widget abs" style="top:1129px;height:322px">
  <h3 style="border-bottom:none">TAGS</h3>
  <div class="tag-cloud">
    <span class="t-s t-c">body language</span>
    <span class="t-l t-r">capsule wardrobe</span>
    <span class="t-s t-g">confidence</span><span class="t-s t-c">handshake</span><span class="t-s t-g">mindset</span><span class="t-s t-c">nlp</span>
    <span class="t-s t-c">passion</span><span class="t-l t-m">power pose</span>
    <span class="t-s t-g">presentations</span><span class="t-s t-r">presence</span>
    <span class="t-l t-m">rapport</span><span class="t-s t-c">spring wear</span><span class="t-s t-m">style</span>
    <span class="t-s t-c">values</span><span class="t-s t-r">vision board</span><span class="t-s t-g">warmth</span>
  </div>
</aside>

<aside class="widget abs" style="top:1490px;height:741px">
  <h3 style="border-bottom:none">COMING UP!</h3>
  <div class="promo">
    <div class="photo" role="img" aria-label="Black and white portrait of Mira smiling"></div>
    <div class="strap"><p>Unlock the<br>superpower<br>of charisma</p></div>
    <div class="live">LIVE</div>
    <p class="places">* Only 6 places left.</p>
    <div class="more">LEARN MORE</div>
  </div>
</aside>

<section class="signup abs">
  <h4>Hey! Don't go without signing up because you'll miss out on exclusive offers,<br>awesome tips, and weekly motivation in my fab newsletter *.</h4>
  <div class="field f1 abs">First Name</div>
  <div class="field f2 abs">Email Address</div>
  <div class="btn-red go abs">Yes Please</div>
  <p class="sad">* And that'll make me sad :-(</p>
</section>

<footer class="site-footer abs">
  <p class="copy abs">© 2016 Mira Haskett Ltd</p>
  <div class="legal abs"><span>Privacy Policy</span><span>Terms Policy</span><span>Terms Policy</span><span>Disclaimers</span></div>
  <div class="social abs"><span></span><span></span><span></span><span></span><span></span></div>
</footer>

</body>
</html>
```